Church Invite (Business Sized)

I would like to get a design for a church invite card. The design should be able to be used on business sized cards. The front should include the "Zephra" logo provided with the phrase "You're Welcomed Here". The back should include the church logo, name, address, phone number, and website.

Church Name: Morningbrook Restoration Chapel
Church Address: 1187 Tollgate Lane, Decatur, GA, 30871
Church Number: 555-017-3926
Church Website: www.mrcministry.example

```html
<!DOCTYPE html>
<html lang="en">
<head>
<meta charset="utf-8">
<title>Zephra Church Invite Card</title>
<link href="https://fonts.googleapis.com/css2?family=Playfair+Display:wght@700;900&display=swap" rel="stylesheet">
<style>
  :root {
    --backdrop: #a0a0a0;
    --paper: #ffffff;
    --sky: #00adeb;
    --sky-light: #45c0ec;
    --ink: #231f20;
    --ink-soft: #363436;
    --cyan: #00b0d8;
    --royal: #0068b5;
  }
  html, body {
    margin: 0;
    width: 1200px;
    height: 900px;
    overflow: hidden;
    background: var(--backdrop);
  }
  .canvas {
    position: relative;
    width: 1200px;
    height: 900px;
  }
  .card {
    position: absolute;
    top: 284px;
    width: 553px;
    height: 332px;
    background: var(--paper);
  }
  .card--front { left: 26px; }
  .card--back { left: 620px; }
  .card svg { display: block; width: 100%; height: 100%; }
  .display {
    font-family: "Playfair Display", Georgia, serif;
    font-weight: 900;
  }
  .brand-name { fill: var(--ink); font-size: 150px; letter-spacing: 2px; }
  .tagline { fill: var(--ink); font-size: 46px; }
  .church-name { fill: var(--royal); font-size: 34px; letter-spacing: 1px; }
  .address { fill: var(--royal); font-size: 31px; }
  .contact { fill: var(--cyan); font-size: 29px; }
</style>
</head>
<body>
<main class="canvas">

  <section class="card card--front" aria-label="Card front">
    <svg viewBox="0 0 921 553" preserveAspectRatio="none">
      <polygon class="band-top-light" fill="var(--sky-light)" points="0,0 921,0 921,24 123,150"/>
      <polygon class="band-top" fill="var(--sky)" points="0,0 921,0 921,24 121,119"/>
      <polygon class="band-bottom-soft" fill="var(--ink-soft)" points="0,527 799,404 921,553 0,553"/>
      <polygon class="band-bottom" fill="var(--ink)" points="0,527 798,434 921,553 0,553"/>
      <text class="display brand-name" x="456" y="322" text-anchor="middle">Zephra</text>
      <text class="display tagline" x="452" y="389" text-anchor="middle">You're Welcomed Here</text>
    </svg>
  </section>

  <section class="card card--back" aria-label="Card back">
    <svg viewBox="0 0 922 553" preserveAspectRatio="none">
      <polygon class="edge-left-dark" fill="var(--royal)" points="0,0 148,127 25,553 0,553"/>
      <polygon class="edge-left" fill="var(--cyan)" points="0,0 120,127 25,553 0,553"/>
      <polygon class="edge-right-light" fill="var(--cyan)" points="922,0 776,127 897,553 922,553"/>
      <polygon class="edge-right" fill="var(--royal)" points="922,0 804,125 897,553 922,553"/>

      <circle class="church-mark" cx="462" cy="110" r="52" fill="var(--royal)"/>
      <text class="display church-name" x="462" y="212" text-anchor="middle">Morningbrook</text>
      <text class="display church-name" x="462" y="250" text-anchor="middle">Restoration Chapel</text>

      <g class="icon-pin" transform="translate(462 305)" fill="var(--royal)">
        <path d="M0,26 C-10,12 -17,2 -17,-7 A17,17 0 0 1 17,-7 C17,2 10,12 0,26 Z"/>
        <circle cx="0" cy="-7" r="6.5" fill="var(--paper)"/>
      </g>
      <text class="display address" x="462" y="372" text-anchor="middle">1187 Tollgate Lane,</text>
      <text class="display address" x="462" y="409" text-anchor="middle">Decatur, GA, 30871</text>

      <g class="icon-phone" transform="translate(199 417) rotate(-45)" fill="var(--cyan)">
        <path d="M-20,-8 a6,6 0 0 1 6,-6 h8 v10 h-6 v8 h6 v10 h-8 a6,6 0 0 1 -6,-6 z" transform="rotate(90)"/>
      </g>
      <text class="display contact" x="204" y="482" text-anchor="middle">555 - 017 - 3926</text>

      <polygon class="icon-cursor" fill="var(--cyan)" points="703,404 742,414 730,422 746,438 738,446 722,430 713,442"/>
      <text class="display contact" x="712" y="482" text-anchor="middle" font-size="25">www.mrcministry.example</text>
    </svg>
  </section>

</main>
</body>
</html>
```